electronic happy holidays card

Need a quick designed holiday card that we can email out and post to our social medias. We are a mobile thermal printer company based in Michigan. We sell to resellers and endusers worldwide. The card needs to say happy holidays or season greetings.

Needs to say in the card: "Wishing you a happy holiday season with all the best wishes for the New Year.

Your friends at Quorvane, LLC.

Target Market(s)

resellers, distributors, end-users world wide.

Industry/Entity Type

Electronic

```html
<!DOCTYPE html>
<html lang="en">
<head>
<meta charset="utf-8">
<title>Quorvane Holiday Card – Build Sequence</title>
<link rel="stylesheet" href="https://fonts.googleapis.com/css2?family=Raleway:wght@300;700;800&family=Kaushan+Script&family=Permanent+Marker&display=swap">
<style>
  :root{
    --blue:#1a8ad4;
    --blue-light:#5db4e6;
    --blue-pale:#8fcaf0;
    --number:#2f8fd2;
    --ink:#1c1c1c;
    --paper:#ffffff;
    --rule:#e3ecf3;
    --maze:#e9ebed;
    --maze-tint:#d3e6f4;
  }
  *{box-sizing:border-box;margin:0;padding:0}
  html,body{width:1200px;height:531px;overflow:hidden;background:var(--paper)}
  body{position:relative;font-family:"Raleway",Arial,sans-serif}

  .step{position:absolute;width:171px;height:266px;border-right:1px solid var(--rule)}
  .step--top{top:0;border-bottom:1px solid var(--rule)}
  .step--bottom{top:265px}
  .step__number{position:absolute;left:6px;font-size:17px;color:var(--number);font-weight:300;line-height:1}
  .step--top .step__number{top:4px}
  .step--bottom .step__number{top:244px}
  .step__panel{position:absolute;left:0;width:171px;height:240px;overflow:hidden}
  .step--top .step__panel{top:24px}
  .step--bottom .step__panel{top:0}

  .card{position:absolute;left:0;top:0;width:171px;height:189px;background:var(--blue);color:var(--paper);text-align:center}
  .step--bottom .card{height:191px}
  .card--final{background:linear-gradient(160deg,var(--blue) 0%,var(--blue-light) 70%,var(--blue-pale) 100%)}

  .greeting{position:absolute;left:0;width:100%;display:flex;align-items:center;justify-content:center;gap:5px}
  .greeting__bar{width:28px;height:5px;background:repeating-linear-gradient(135deg,rgba(255,255,255,.9) 0 2px,transparent 2px 4px)}
  .greeting__intro{top:16px;font-size:9px;font-style:italic;font-weight:300}
  .greeting__happy{position:absolute;left:0;width:100%;top:30px;font-family:"Kaushan Script",cursive;font-size:31px;line-height:1}
  .greeting__holidays{top:71px;font-size:7px;font-weight:800;letter-spacing:1px}
  .greeting__holidays .greeting__bar{width:34px}
  .greeting__divider{position:absolute;left:25px;width:121px;top:91px;height:1px;background:rgba(255,255,255,.6)}
  .greeting__amp{position:absolute;left:79px;top:85px;width:13px;height:13px;border-radius:50%;background:var(--paper);color:var(--blue);font-size:8px;font-weight:800;line-height:13px}
  .greeting__successful{position:absolute;left:0;width:100%;top:99px;font-size:16px;font-weight:300;color:var(--blue-pale);letter-spacing:.5px}
  .greeting__new{position:absolute;left:0;width:100%;top:115px;font-family:"Permanent Marker",cursive;font-size:27px;line-height:1.1}
  .greeting__year{position:absolute;left:0;width:100%;top:146px;font-family:"Kaushan Script",cursive;font-size:12px}
  .greeting__date{position:absolute;left:45px;width:81px;top:170px;height:11px;border-top:1px solid rgba(255,255,255,.7);border-bottom:1px solid rgba(255,255,255,.7);font-size:7px;line-height:9px;font-weight:700;letter-spacing:1px}

  .brand{position:absolute;left:0;width:171px;display:flex;align-items:center;justify-content:center;gap:6px;color:var(--ink);font-weight:800;font-size:17px;letter-spacing:.5px}
  .step--top .brand{top:202px}
  .step--bottom .brand{top:205px}
  .brand__mark{width:13px;height:13px;background:var(--blue)}

  .maze{position:absolute;width:110px;background:linear-gradient(180deg,var(--maze-tint) 0%,var(--maze) 55%)}
  .step--top .maze{left:31px;top:38px;height:175px}
  .step--bottom .maze{left:30px;top:35px;height:205px}
</style>
</head>
<body>

<section class="step step--top" style="left:0"><span class="step__number">1</span>
  <div class="step__panel"><div class="card"></div>
    <div class="brand"><span class="brand__mark"></span>QUORVANE</div></div></section>

<section class="step step--top" style="left:171px"><span class="step__number">2</span>
  <div class="step__panel"><div class="maze" role="img" aria-label="Maze with a star at the top entrance, no path drawn yet"></div></div></section>

<section class="step step--top" style="left:343px"><span class="step__number">3</span>
  <div class="step__panel"><div class="card">
    <p class="greeting greeting__intro"><span class="greeting__bar"></span>We wish you<span class="greeting__bar"></span></p>
  </div><div class="brand"><span class="brand__mark"></span>QUORVANE</div></div></section>

<section class="step step--top" style="left:514px"><span class="step__number">4</span>
  <div class="step__panel"><div class="maze" role="img" aria-label="Maze with the first blue path branches forming the tip of a tree"></div></div></section>

<section class="step step--top" style="left:685px"><span class="step__number">5</span>
  <div class="step__panel"><div class="card">
    <p class="greeting greeting__intro"><span class="greeting__bar"></span>We wish you<span class="greeting__bar"></span></p>
    <h1 class="greeting__happy">Happy</h1>
    <p class="greeting greeting__holidays"><span class="greeting__bar"></span>HOLIDAYS<span class="greeting__bar"></span></p>
  </div><div class="brand"><span class="brand__mark"></span>QUORVANE</div></div></section>

<section class="step step--top" style="left:856px"><span class="step__number">6</span>
  <div class="step__panel"><div class="maze" role="img" aria-label="Maze with a blue path growing into the upper part of a tree"></div></div></section>

<section class="step step--top" style="left:1027px;border-right:0"><span class="step__number">7</span>
  <div class="step__panel"><div class="card">
    <p class="greeting greeting__intro"><span class="greeting__bar"></span>We wish you<span class="greeting__bar"></span></p>
    <h1 class="greeting__happy">Happy</h1>
    <p class="greeting greeting__holidays"><span class="greeting__bar"></span>HOLIDAYS<span class="greeting__bar"></span></p>
    <span class="greeting__divider"></span><span class="greeting__amp">&amp;</span>
    <p class="greeting__successful">SUCCESSFUL</p>
  </div><div class="brand"><span class="brand__mark"></span>QUORVANE</div></div></section>

<section class="step step--bottom" style="left:0"><span class="step__number">8</span>
  <div class="step__panel"><div class="maze" role="img" aria-label="Maze with a blue path forming half of a tree"></div></div></section>

<section class="step step--bottom" style="left:171px"><span class="step__number">9</span>
  <div class="step__panel"><div class="card">
    <p class="greeting greeting__intro"><span class="greeting__bar"></span>We wish you<span class="greeting__bar"></span></p>
    <h1 class="greeting__happy">Happy</h1>
    <p class="greeting greeting__holidays"><span class="greeting__bar"></span>HOLIDAYS<span class="greeting__bar"></span></p>
    <span class="greeting__divider"></span><span class="greeting__amp">&amp;</span>
    <p class="greeting__successful">SUCCESSFUL</p>
    <p class="greeting__new">NEW</p>
  </div><div class="brand"><span class="brand__mark"></span>QUORVANE</div></div></section>

<section class="step step--bottom" style="left:343px"><span class="step__number">10</span>
  <div class="step__panel"><div class="maze" role="img" aria-label="Maze with a blue path forming most of a tree"></div></div></section>

<section class="step step--bottom" style="left:514px"><span class="step__number">11</span>
  <div class="step__panel"><div class="card">
    <p class="greeting greeting__intro"><span class="greeting__bar"></span>We wish you<span class="greeting__bar"></span></p>
    <h1 class="greeting__happy">Happy</h1>
    <p class="greeting greeting__holidays"><span class="greeting__bar"></span>HOLIDAYS<span class="greeting__bar"></span></p>
    <span class="greeting__divider"></span><span class="greeting__amp">&amp;</span>
    <p class="greeting__successful">SUCCESSFUL</p>
    <p class="greeting__new">NEW</p>
    <p class="greeting__year">year</p>
  </div><div class="brand"><span class="brand__mark"></span>QUORVANE</div></div></section>

<section class="step step--bottom" style="left:685px"><span class="step__number">12</span>
  <div class="step__panel"><div class="maze" role="img" aria-label="Maze with a blue path forming a nearly complete tree"></div></div></section>

<section class="step step--bottom" style="left:856px"><span class="step__number">13</span>
  <div class="step__panel"><div class="card card--final">
    <p class="greeting greeting__intro"><span class="greeting__bar"></span>We wish you<span class="greeting__bar"></span></p>
    <h1 class="greeting__happy">Happy</h1>
    <p class="greeting greeting__holidays"><span class="greeting__bar"></span>HOLIDAYS<span class="greeting__bar"></span></p>
    <span class="greeting__divider"></span><span class="greeting__amp">&amp;</span>
    <p class="greeting__successful">SUCCESSFUL</p>
    <p class="greeting__new">NEW</p>
    <p class="greeting__year">year</p>
    <p class="greeting__date">2015</p>
  </div><div class="brand"><span class="brand__mark"></span>QUORVANE</div></div></section>

<section class="step step--bottom" style="left:1027px;border-right:0"><span class="step__number">14</span>
  <div class="step__panel"><div class="maze" role="img" aria-label="Maze with the finished blue path forming a full Christmas tree under a star"></div></div></section>

</body>
</html>
```